Changes to wine label

Need existing labels designed by Pixel Harbor corrected to meet QRV.

Target Market(s)

Wine drinkers

Requirements
Must have
• Use attached label design. A. Label #2 spelling correct" Zinfandel". Also, 500ml instead of 375ml and place on front label with so would be 500ml/Alcohol %18 By Volume. Remove residual sugar text.
Should not have
• Sorrel Bluff LOGO on both label#1 & #2 different red that pops the log. And an addtional label with the white grapes

```html
<!DOCTYPE html>
<html lang="en">
<head>
<meta charset="utf-8">
<title>Sorrel Bluff Mead Co – Wine Labels</title>
<link rel="stylesheet" href="https://fonts.googleapis.com/css2?family=Tinos:ital,wght@0,400;0,700;1,400&family=Open+Sans:ital,wght@0,400;0,700;1,400&display=swap">
<style>
  :root {
    --backdrop: #331615;
    --label-black: #0b0b0b;
    --label-glow: #2a2a2a;
    --crimson: #9c1b2e;
    --gold: #d9a53a;
    --ink-white: #f4f1ec;
    --grape-red-1: #d27ab4;
    --grape-red-2: #8a3f73;
    --grape-gold-1: #f4c531;
    --grape-gold-2: #c9541d;
    --seal-1: #e6c56a;
    --seal-2: #a8832e;
  }
  * { box-sizing: border-box; margin: 0; padding: 0; }
  html, body {
    width: 1200px; height: 600px; overflow: hidden;
    background: var(--backdrop);
  }
  .canvas { position: relative; width: 1200px; height: 600px; }

  .label {
    position: absolute; top: 109px;
    width: 337px; height: 405px;
    background:
      radial-gradient(ellipse 60% 45% at 50% 55%, var(--label-glow) 0%, var(--label-black) 75%);
    box-shadow: 2px 3px 6px rgba(0,0,0,.45);
    font-family: "Tinos", serif;
  }
  .label--red { left: 94px; }
  .label--white { left: 445px; }
  .label--back { left: 797px; background: radial-gradient(ellipse 70% 40% at 50% 25%, var(--label-glow) 0%, var(--label-black) 80%); }

  .brand { position: absolute; left: 0; right: 0; text-align: center; color: var(--crimson); font-family: "Tinos", serif; font-weight: 400; text-transform: uppercase; }
  .brand__name { display: block; font-size: 25px; letter-spacing: 3px; line-height: 1; }
  .brand__sub { display: block; font-size: 16px; letter-spacing: 7px; margin-top: 9px; line-height: 1; }
  .label--red .brand, .label--white .brand { top: 74px; }
  .label--white .brand { top: 71px; }
  .label--back .brand { top: 55px; }
  .label--back .brand__name { font-size: 19px; letter-spacing: 2px; }
  .label--back .brand__sub { font-size: 12px; letter-spacing: 5px; margin-top: 5px; }

  .grape-art {
    position: absolute; left: 89px; top: 155px; width: 160px; height: 162px;
    border-radius: 45% 55% 50% 50% / 40% 45% 60% 60%;
  }
  .label--red .grape-art { background: radial-gradient(circle at 45% 40%, var(--grape-red-1), var(--grape-red-2)); }
  .label--white .grape-art { background: radial-gradient(circle at 45% 40%, var(--grape-gold-1), var(--grape-gold-2)); }

  .front-footer { position: absolute; left: 0; right: 0; top: 366px; height: 30px; }
  .volume { position: absolute; left: 44px; top: 6px; font-size: 8px; color: var(--gold); }
  .style-name { position: absolute; left: 0; right: 0; top: 0; text-align: center; font-size: 17px; letter-spacing: .5px; }
  .label--red .style-name { color: var(--crimson); }
  .label--white .style-name { color: var(--gold); top: 4px; }
  .abv { position: absolute; right: 22px; top: 6px; font-size: 8px; color: var(--gold); text-align: center; line-height: 1.15; }
  .abv small { display: block; font-size: 7px; }

  .back-copy { position: absolute; left: 0; right: 0; color: var(--ink-white); text-align: center; }
  .varietal { top: 102px; font-size: 11px; font-weight: 700; line-height: 1.05; }
  .tasting-note { top: 132px; font-size: 15px; line-height: 15px; white-space: nowrap; }
  .producer { top: 236px; font-family: "Open Sans", sans-serif; font-style: italic; font-size: 8px; line-height: 1.4; letter-spacing: -.2px; }
  .warning {
    position: absolute; left: 17px; right: 22px; top: 272px;
    font-family: "Open Sans", sans-serif; font-size: 10px; line-height: 14px; color: var(--ink-white);
  }
  .warning strong { font-weight: 700; }
  .back-meta { position: absolute; left: 17px; right: 24px; top: 344px; font-family: "Open Sans", sans-serif; font-size: 8.5px; color: var(--ink-white); display: flex; justify-content: space-between; }
  .seal {
    position: absolute; left: 145px; top: 351px; width: 40px; height: 40px; border-radius: 50%;
    background: radial-gradient(circle at 40% 35%, var(--seal-1), var(--seal-2));
  }
</style>
</head>
<body>
<main class="canvas">

  <section class="label label--red">
    <div class="brand"><span class="brand__name">Sorrel Bluff</span><span class="brand__sub">Mead Co</span></div>
    <div class="grape-art" role="img" aria-label="Painted illustration of a bunch of red grapes with a green stem"></div>
    <div class="front-footer">
      <span class="volume">500ML</span>
      <span class="style-name">RED WINE</span>
      <span class="abv">ALCOHOL %18<small>by volume</small></span>
    </div>
  </section>

  <section class="label label--white">
    <div class="brand"><span class="brand__name">Sorrel Bluff</span><span class="brand__sub">Mead Co</span></div>
    <div class="grape-art" role="img" aria-label="Painted illustration of a bunch of golden white grapes with a green stem"></div>
    <div class="front-footer">
      <span class="volume">500ML</span>
      <span class="style-name">WHITE WINE</span>
      <span class="abv">ALCOHOL %18<small>by volume</small></span>
    </div>
  </section>

  <section class="label label--back">
    <div class="brand"><span class="brand__name">Sorrel Bluff</span><span class="brand__sub">Mead Co</span></div>
    <p class="back-copy varietal">CALIFORNIA<br>ZINFANDEL 50% SYRAH 50%.</p>
    <p class="back-copy tasting-note">A fruit forward dessert style wine that<br>takes the aroma of the varitals and balances<br>it with sweetness and zealous acidity.<br>Meant to be drunk young or slightly aged,<br>complementary with cheeses and chocolate.</p>
    <p class="back-copy producer">PRODUCED AND BOTTLED BY<br>SORREL BLUFF MEAD CO. ALDER CREEK, CALIFORNIA</p>
    <p class="warning"><strong>GOVERNMENT WARNING:</strong> (1) According to the Surgeon General, women should not drink alcoholic beverages during pregnancy because of the risk of birth defects. (2) Consumption of alcoholic beverages impairs your ability to drive a car or operate machinery, and may cause health problems.</p>
    <div class="back-meta"><span>500ML</span><span>CONTAINS SULFITES</span></div>
    <div class="seal" aria-hidden="true"></div>
  </section>

</main>
</body>
</html>
```